Medical Device - Case Study Template

We need a TEMPLATE that we can reuse to write various case studies about the medical equipment solutions we provide. It will be a double sided letter sized with a modern design that conveys a feeling of expertise, innovation and highly personable service AND be consistent with the brand guide. The content will be divided into a few sections:

- Situation (200-250 words)
- Challenge (100-120 words)
- Solution (100-120 words)
- Results (100-120 words)
- Conclusion (100-120 words)

Additionally, there will need to be a call to action, inviting people to send an email for more information and a short "About Talvo" section (approx. 40 words).

For device picture placeholders, feel free to use any random small benchtop medical device.

```html
<!DOCTYPE html>
<html lang="en">
<head>
<meta charset="utf-8">
<title>Talvo – Case Study Template</title>
<link rel="stylesheet" href="https://fonts.googleapis.com/css2?family=Nunito:wght@800;900&family=Open+Sans:wght@400;600;700&display=swap">
<style>
  :root{
    --stage:#ececec;
    --paper:#ffffff;
    --header-blue:#132a8e;
    --header-num:#2a45a8;
    --navy:#0c2461;
    --heading:#10296b;
    --rule:#21336f;
    --ink:#1c1c1c;
    --orange:#f47b20;
    --photo-a:#2b3e9c;
    --photo-b:#8a8f9e;
  }
  *{box-sizing:border-box;margin:0;padding:0}
  html,body{width:1200px;height:720px;overflow:hidden}
  body{background:linear-gradient(180deg,#f4f4f4,#e2e2e2);font-family:"Open Sans",sans-serif;color:var(--ink);position:relative}

  .page{position:absolute;top:38px;width:499px;height:646px;background:var(--paper);overflow:hidden;box-shadow:0 2px 6px rgba(0,0,0,.25)}
  .page--front{left:65px}
  .page--back{left:635px}

  .masthead{position:absolute;left:0;top:0;width:100%;height:112px;background:var(--header-blue);overflow:hidden}
  .masthead__photo{position:absolute;left:0;top:0;width:150px;height:100px;background:radial-gradient(ellipse at 55% 40%,var(--photo-b) 0%,var(--photo-a) 70%);opacity:.9;border-bottom-right-radius:40px}
  .brand{position:absolute;display:flex;align-items:center;gap:5px;color:#fff}
  .brand__dot{width:16px;height:16px;border-radius:50%;background:var(--orange);flex:none}
  .brand__text{display:flex;flex-direction:column;line-height:1}
  .brand__name{font-family:"Open Sans",sans-serif;font-weight:600;font-size:20px;letter-spacing:.5px}
  .brand__tag{font-size:6.5px;letter-spacing:.6px;margin-top:2px;text-align:right}
  .masthead .brand{left:335px;top:17px}
  .masthead__title{position:absolute;left:298px;top:66px;font-family:"Nunito",sans-serif;font-weight:900;font-size:25px;color:#fff;letter-spacing:-.3px}
  .masthead__num{position:absolute;right:16px;top:70px;font-family:"Nunito",sans-serif;font-weight:900;font-size:52px;line-height:1;color:var(--header-num)}
  .page--back .masthead__num{right:10px}

  .section-title{position:absolute;left:21px;font-family:"Nunito",sans-serif;font-weight:800;font-size:17px;color:var(--heading);letter-spacing:-.2px}
  .panel{position:absolute;left:21px;width:465px}
  .panel__frame{position:absolute;left:0;top:0}
  .panel__body{position:relative;padding:4px 8px 0 5px;font-size:7.9px;line-height:9px}
  .panel__body p + p{margin-top:9px}

  .footer-band{position:absolute;left:0;bottom:0}

  .about__title{position:absolute;right:32px;top:409px;padding:0 8px;background:var(--paper);font-family:"Nunito",sans-serif;font-weight:800;font-size:16.5px;color:var(--heading)}
  .about__body{position:absolute;left:21px;top:430px;width:452px;text-align:right;font-size:9.6px;line-height:14.6px}

  .cta{position:absolute;left:20px;top:511px;width:274px;height:60px;color:#fff}
  .cta__shape{position:absolute;left:0;top:0}
  .cta__icon{position:absolute;left:10px;top:13px}
  .cta__lead{position:absolute;left:93px;top:13px;font-size:9.3px}
  .cta__email{position:absolute;left:93px;top:28px;font-size:13px;font-weight:700}

  .footer .brand{position:absolute;top:617px;right:24px}
</style>
</head>
<body>

<!-- Front side -->
<section class="page page--front">
  <header class="masthead">
    <div class="masthead__photo" role="img" aria-label="Photo of a stethoscope and wrist blood pressure monitor"></div>
    <div class="brand"><span class="brand__dot"></span><span class="brand__text"><span class="brand__name">talvo</span><span class="brand__tag">Medical Technology</span></span></div>
    <h1 class="masthead__title">CASE STUDY</h1>
    <span class="masthead__num">1</span>
  </header>

  <h2 class="section-title" style="top:134px">Situation</h2>
  <div class="panel" style="top:160px;height:178px">
    <svg class="panel__frame" width="465" height="178"><polygon points="0.5,0.5 464.5,0.5 464.5,154 441,177.5 0.5,177.5" fill="none" stroke="var(--rule)" stroke-width="1"/></svg>
    <div class="panel__body">
      <p>Lorem ipsum dolor sit amet, consectetur adipiscing elit. Fusce tristique, ex ac elementum sodales, velit est imperdiet leo, eu aliquet felis leo in tortor. Sed vel nisl id metus fringilla egestas. Phasellus euismod, velit sit amet ullamcorper pellentesque, tellus ante ullamcorper risus, at bibendum elit odio vitae nisl. Fusce cursus faucibus mi, sit amet commodo est dapibus at. Pellentesque nec nulla nunc. Duis ornare dapibus elementum. Mauris eu mauris sit amet urna vulputate maximus ut ut elit. Mauris porta sagittis elit, quis rhoncus turpis vulputate et. Nunc ante neque, dignissim id ante non, interdum feugiat mauris. Quisque ornare vitae justo cursus pulvinar. Duis posuere augue arcu, et rhoncus orci volutpat sed. Mauris id posuere eros.</p>
      <p>Aliquam erat volutpat. Phasellus egestas pellentesque eleifend. Praesent at posuere lorem. Nunc ornare ultricies felis, vel semper nisl blandit et. Interdum et malesuada fames ac ante ipsum primis in faucibus. Pellentesque arcu est, iaculis sit amet sagittis quis, porta quis lectus. Donec quis imperdiet erat. Proin non ex felis. Aenean blandit turpis a vestibulum consequat. Integer a finibus neque, ut blandit metus. In dignissim lacus in urna blandit fringilla. Suspendisse sem tellus, mollis vitae dictum ac, suscipit nec metus.</p>
      <p>Nam metus velit, condimentum eu aliquam ut, convallis quis ipsum. Praesent cursus nunc condimentum massa porttitor cursus. Proin eu rutrum eros. Aenean imperdiet dapibus nisl sed placerat. Pellentesque habitant morbi tristique senectus et netus et malesuada fames ac turpis egestas. Cras rutrum libero et libero porta suscipit. In hac habitasse platea dictumst. Aenean at convallis lorem</p>
    </div>
  </div>

  <h2 class="section-title" style="top:352px">Challenge</h2>
  <div class="panel" style="top:377px;height:75px">
    <svg class="panel__frame" width="465" height="75"><polygon points="0.5,0.5 464.5,0.5 464.5,52 445,74.5 0.5,74.5" fill="none" stroke="var(--rule)" stroke-width="1"/></svg>
    <div class="panel__body"><p>Lorem ipsum dolor sit amet, consectetur adipiscing elit. Aliquam quis porttitor nibh. Ut viverra sollicitudin gravida. Praesent elementum, odio et finibus feugiat, odio sapien consequat leo, at cursus mauris diam in arcu. Integer ex purus, vestibulum et ultricies non, mollis sit amet orci. Morbi et dolor quis ex volutpat suscipit a nec lacus. Duis quis eros rutrum, convallis elit eu, fringilla dolor. Nunc interdum nisl eu nisi fringilla, at elementum libero laoreet. Pellentesque aliquam tristique nibh id ultrices. Nunc sed purus at ante aliquam cursus non a sem. Aliquam nec sagittis ligula. In hac habitasse platea dictumst. Nam placerat ultrices ligula vel pharetra. Nulla facilisi. Proin sit amet auctor elit, et condimentum nulla. Pellentesque risus eros, volutpat quis posuere a.</p></div>
  </div>

  <h2 class="section-title" style="top:472px">Solution</h2>
  <div class="panel" style="top:498px;height:75px">
    <svg class="panel__frame" width="465" height="75"><polygon points="0.5,0.5 464.5,0.5 464.5,52 445,74.5 0.5,74.5" fill="none" stroke="var(--rule)" stroke-width="1"/></svg>
    <div class="panel__body"><p>Lorem ipsum dolor sit amet, consectetur adipiscing elit. Aliquam quis porttitor nibh. Ut viverra sollicitudin gravida. Praesent elementum, odio et finibus feugiat, odio sapien consequat leo, at cursus mauris diam in arcu. Integer ex purus, vestibulum et ultricies non, mollis sit amet orci. Morbi et dolor quis ex volutpat suscipit a nec lacus. Duis quis eros rutrum, convallis elit eu, fringilla dolor. Nunc interdum nisl eu nisi fringilla, at elementum libero laoreet. Pellentesque aliquam tristique nibh id ultrices. Nunc sed purus at ante aliquam cursus non a sem. Aliquam nec sagittis ligula. In hac habitasse platea dictumst. Nam placerat ultrices ligula vel pharetra. Nulla facilisi. Proin sit amet auctor elit, et condimentum nulla. Pellentesque risus eros, volutpat quis posuere a.</p></div>
  </div>

  <footer class="footer">
    <svg class="footer-band" width="499" height="76" viewBox="0 0 499 76"><polygon points="0,37 475,37 499,0 499,76 0,76" fill="var(--navy)"/><line x1="0" y1="36" x2="474" y2="36" stroke="#9aa6c8" stroke-width="1"/></svg>
    <div class="brand"><span class="brand__dot"></span><span class="brand__text"><span class="brand__name">talvo</span><span class="brand__tag">Medical Technology</span></span></div>
  </footer>
</section>

<!-- Back side -->
<section class="page page--back">
  <header class="masthead">
    <div class="masthead__photo" role="img" aria-label="Photo of a stethoscope and wrist blood pressure monitor"></div>
    <div class="brand" style="left:328px"><span class="brand__dot"></span><span class="brand__text"><span class="brand__name">talvo</span><span class="brand__tag">Medical Technology</span></span></div>
    <h1 class="masthead__title" style="left:292px">CASE STUDY</h1>
    <span class="masthead__num">2</span>
  </header>

  <h2 class="section-title" style="top:134px">Results</h2>
  <div class="panel" style="top:160px;height:75px">
    <svg class="panel__frame" width="465" height="75"><polygon points="0.5,0.5 464.5,0.5 464.5,52 445,74.5 0.5,74.5" fill="none" stroke="var(--rule)" stroke-width="1"/></svg>
    <div class="panel__body"><p>Lorem ipsum dolor sit amet, consectetur adipiscing elit. Aliquam quis porttitor nibh. Ut viverra sollicitudin gravida. Praesent elementum, odio et finibus feugiat, odio sapien consequat leo, at cursus mauris diam in arcu. Integer ex purus, vestibulum et ultricies non, mollis sit amet orci. Morbi et dolor quis ex volutpat suscipit a nec lacus. Duis quis eros rutrum, convallis elit eu, fringilla dolor. Nunc interdum nisl eu nisi fringilla, at elementum libero laoreet. Pellentesque aliquam tristique nibh id ultrices. Nunc sed purus at ante aliquam cursus non a sem. Aliquam nec sagittis ligula. In hac habitasse platea dictumst. Nam placerat ultrices ligula vel pharetra. Nulla facilisi. Proin sit amet auctor elit, et condimentum nulla. Pellentesque risus eros, volutpat quis posuere a.</p></div>
  </div>

  <h2 class="section-title" style="top:254px">Conclusion</h2>
  <div class="panel" style="top:280px;height:75px">
    <svg class="panel__frame" width="465" height="75"><polygon points="0.5,0.5 464.5,0.5 464.5,52 445,74.5 0.5,74.5" fill="none" stroke="var(--rule)" stroke-width="1"/></svg>
    <div class="panel__body"><p>Lorem ipsum dolor sit amet, consectetur adipiscing elit. Aliquam quis porttitor nibh. Ut viverra sollicitudin gravida. Praesent elementum, odio et finibus feugiat, odio sapien consequat leo, at cursus mauris diam in arcu. Integer ex purus, vestibulum et ultricies non, mollis sit amet orci. Morbi et dolor quis ex volutpat suscipit a nec lacus. Duis quis eros rutrum, convallis elit eu, fringilla dolor. Nunc interdum nisl eu nisi fringilla, at elementum libero laoreet. Pellentesque aliquam tristique nibh id ultrices. Nunc sed purus at ante aliquam cursus non a sem. Aliquam nec sagittis ligula. In hac habitasse platea dictumst. Nam placerat ultrices ligula vel pharetra. Nulla facilisi. Proin sit amet auctor elit, et condimentum nulla. Pellentesque risus eros, volutpat quis posuere a.</p></div>
  </div>

  <svg class="panel__frame" style="position:absolute;left:21px;top:417px" width="465" height="72"><polyline points="335,0.5 0.5,0.5 0.5,71.5 464.5,71.5 464.5,0.5 445,0.5" fill="none" stroke="var(--rule)" stroke-width="1"/></svg>
  <h2 class="about__title">About Talvo</h2>
  <p class="about__body">Lorem ipsum dolor sit amet, consectetur adipiscing elit. Nullam scelerisque neque massa. Phasellus nec tempor mauris. Quisque malesuada diam lacinia blandit tempus. Nullam fringilla ligula vitae magna viverra, nec ornare urna elementum. Morbi sed ullamcorper enim. In tincidunt dui facilisis.</p>

  <div class="cta">
    <svg class="cta__shape" width="274" height="60"><polygon points="0,0 274,0 274,42 264,60 0,60" fill="var(--navy)"/></svg>
    <svg class="cta__icon" width="70" height="36" viewBox="0 0 70 36" fill="none" stroke="#fff" stroke-width="2" stroke-linejoin="round">
      <polygon points="26,6 66,2 68,28 28,32"/>
      <polyline points="26,6 48,20 66,2"/>
      <line x1="2" y1="14" x2="20" y2="14"/><line x1="6" y1="19" x2="22" y2="19"/><line x1="10" y1="24" x2="24" y2="24"/><line x1="14" y1="29" x2="25" y2="29"/>
    </svg>
    <span class="cta__lead">Email us for more information</span>
    <span class="cta__email">info@talvomedical.com</span>
  </div>

  <footer class="footer">
    <svg class="footer-band" width="499" height="76" viewBox="0 0 499 76"><polygon points="0,37 475,37 499,0 499,76 0,76" fill="var(--navy)"/><line x1="0" y1="36" x2="474" y2="36" stroke="#9aa6c8" stroke-width="1"/></svg>
    <div class="brand"><span class="brand__dot"></span><span class="brand__text"><span class="brand__name">talvo</span><span class="brand__tag">Medical Technology</span></span></div>
  </footer>
</section>

</body>
</html>
```